New Look for Existing Website
Keep it simple, clean, crisp & clear
Creative Brief
Automotive
www.bitlocate.ie
We are an advertising website where people search for and view lists of results and associated information for second hand car parts suppliers.
we like Zorvane for its simplicity. We like clean and simple websites, easy to navigate and not cluttered with lots of links/advertisements or too much text.
www.zorvane.ie
http://www.klimbrook.ie/klimbrook/publish/vehicleLookup.jsp
please view the existing website at www.bitlocate.ie and then create new look for the main page/template every are should have its own box/ container with soft borders also logo looks too plain and can be changed if required.

```html
<!DOCTYPE html>
<html lang="en">
<head>
<meta charset="utf-8">
<title>BitLocate.ie – Car Dismantlers &amp; Car Parts Search</title>
<link href="https://fonts.googleapis.com/css2?family=PT+Sans:wght@400;700&display=swap" rel="stylesheet">
<style>
:root{
  --navy:#0d3d8c;
  --navy-dark:#082c69;
  --red:#c8141c;
  --red-dark:#8e0d12;
  --panel:#cddcee;
  --panel-line:#9fb6d4;
  --grey-box:#9a9a9a;
  --grey-text:#eeeeee;
  --text:#1c2a44;
  --page:#f1f2f4;
}
*{box-sizing:border-box;margin:0;padding:0}
html,body{width:1200px;height:763px;overflow:hidden}
body{position:relative;background:linear-gradient(180deg,#e3e5e9 0,var(--page) 30%,#ffffff 70%,#e9ebee 100%);font-family:"PT Sans",Arial,sans-serif;color:var(--text)}
.abs{position:absolute}
.account-bar{left:967px;top:0;width:137px;height:30px;background:var(--navy);border-radius:0 0 6px 6px;display:flex;justify-content:space-around;align-items:center;color:#fff;font-weight:700;font-size:14px}
.logo-box{left:108px;top:67px;width:348px;height:72px;background:#fff;border-radius:8px;box-shadow:0 2px 6px rgba(0,0,0,.15);display:flex;align-items:center;padding-left:26px;gap:14px}
.logo-mark{width:34px;height:34px;border-radius:50%;background:var(--red)}
.logo-name{font-size:42px;font-weight:700;color:var(--navy);letter-spacing:-.5px}
.banner-ad{left:629px;top:72px;width:475px;height:62px;background:var(--grey-box);color:var(--grey-text);font-size:16px;display:flex;align-items:center;justify-content:center}
.main-nav{left:108px;top:154px;width:996px;height:38px;background:linear-gradient(180deg,#1d55ad,var(--navy-dark));border-radius:6px;display:flex;align-items:center;padding-left:66px}
.main-nav a{color:#fff;font-weight:700;font-size:15px;text-decoration:none;padding:4px 10px;border-right:1px solid rgba(255,255,255,.35)}
.main-nav a:last-child{border-right:none}
.main-nav a.active{background:var(--red);border-radius:4px}
.search-panel{left:108px;top:211px;width:720px;height:437px;background:var(--panel);border:2px solid var(--panel-line);border-radius:8px;overflow:hidden}
.panel-art{left:160px;top:110px;width:420px;height:200px;border-radius:90px 90px 30px 30px;background:radial-gradient(ellipse at center,rgba(170,195,225,.55),rgba(205,220,238,0))}
.step-ghost{left:14px;top:90px;font-size:190px;font-weight:700;color:rgba(150,175,210,.35);line-height:1}
.panel-tab{left:105px;top:0;width:615px;height:66px;background:linear-gradient(180deg,#fff,#e8eef6);border-radius:0 0 0 40px;box-shadow:0 2px 4px rgba(0,0,0,.12);display:flex;align-items:center;justify-content:center;color:var(--red);font-weight:700;font-size:22px}
.steps{left:280px;top:103px;display:flex;align-items:center;font-size:15px}
.step{width:27px;height:27px;border-radius:50%;border:2px solid #fff;display:flex;align-items:center;justify-content:center;font-weight:700;color:#fff;background:#a8c0de}
.step.current{background:var(--navy)}
.step-link{width:20px;height:3px;background:#fff}
.steps span.label{margin-right:8px}
.instruction{left:0;top:165px;width:716px;text-align:center;font-size:16px}
.selectors{left:10px;top:205px;display:flex;gap:4px}
.select{width:136px;height:27px;background:#fff;border:2px solid var(--navy);display:flex;justify-content:space-between;align-items:center;padding-left:6px;font-size:11px;font-weight:700}
.select i{width:20px;height:23px;background:var(--navy);display:flex;align-items:center;justify-content:center}
.terms{left:0;top:284px;width:716px;text-align:center;font-size:14px}
.search-btn{left:250px;top:329px;width:284px;height:40px;border-radius:10px;background:linear-gradient(180deg,#e0303a,var(--red) 50%,var(--red-dark));box-shadow:0 2px 4px rgba(0,0,0,.35);color:#fff;font-weight:700;font-size:18px;display:flex;align-items:center;justify-content:center;gap:10px}
.side-ad{left:845px;width:259px;background:var(--grey-box);color:#fff;font-weight:700;font-size:16px;text-align:center;display:flex;align-items:center;justify-content:center;line-height:1.25}
.footer{left:0;top:691px;width:1200px;height:72px;background:linear-gradient(180deg,#1a4fa3,var(--navy-dark));color:#fff}
.social{left:96px;top:14px;display:flex;gap:22px;font-size:11px}
.social div{display:flex;flex-direction:column;align-items:center;gap:2px}
.social b{width:28px;height:28px;border-radius:50%;background:#f2f5fa}
.footer-links{left:432px;top:14px;display:flex;gap:22px;font-size:14px}
.copyright{right:130px;top:22px;text-align:right;font-size:12px;line-height:1.35}
.footer-art{right:36px;top:8px;width:80px;height:50px;border-radius:40px 40px 10px 10px;background:linear-gradient(180deg,rgba(255,255,255,.25),rgba(255,255,255,.05))}
</style>
</head>
<body>
<div class="abs account-bar"><span>Login »</span><span>Sign Up »</span></div>

<div class="abs logo-box"><span class="logo-mark"></span><span class="logo-name">BitLocate.ie</span></div>
<div class="abs banner-ad">banner advertisement</div>

<nav class="abs main-nav">
  <a class="active">Parts Search</a><a>Parts Request</a><a>Damaged Repairables</a><a>About</a><a>Contact</a><a>Dismantlers by Map</a><a>Dismantlers by List</a>
</nav>

<section class="abs search-panel">
  <div class="abs step-ghost">1</div>
  <div class="abs panel-art" role="img" aria-label="Faint car silhouette behind the search form"></div>
  <h1 class="abs panel-tab">Car Dismantlers - Car Parts Search</h1>
  <div class="abs steps"><span class="label">Step</span><span class="step current">1</span><span class="step-link"></span><span class="step">2</span><span class="step-link"></span><span class="step">3</span></div>
  <p class="abs instruction">Select the Make, Model &amp; Year of the vehicle for which you require parts!</p>
  <div class="abs selectors">
    <div class="select">CAR MAKE<i><svg width="10" height="8"><path d="M0 0h10L5 8z" fill="#fff"/></svg></i></div>
    <div class="select">CAR MODEL<i><svg width="10" height="8"><path d="M0 0h10L5 8z" fill="#fff"/></svg></i></div>
    <div class="select">ANY YEAR<i><svg width="10" height="8"><path d="M0 0h10L5 8z" fill="#fff"/></svg></i></div>
    <div class="select">ANY CATEGORY<i><svg width="10" height="8"><path d="M0 0h10L5 8z" fill="#fff"/></svg></i></div>
    <div class="select">ANY PARTS<i><svg width="10" height="8"><path d="M0 0h10L5 8z" fill="#fff"/></svg></i></div>
  </div>
  <p class="abs terms">By clicking the Search button below you are agreeing with the Terms &amp; Conditions</p>
  <div class="abs search-btn">Search Car Dismantlers
    <svg width="20" height="20" viewBox="0 0 20 20"><circle cx="8" cy="8" r="6" fill="none" stroke="#fff" stroke-width="2.5"/><path d="M12.5 12.5l6 6" stroke="#fff" stroke-width="3" stroke-linecap="round"/></svg>
  </div>
</section>

<div class="abs side-ad" style="top:211px;height:190px">Place Your<br>Ad Here</div>
<div class="abs side-ad" style="top:413px;height:257px">Place Parts<br>Request Here</div>

<footer class="abs footer">
  <div class="abs social"><div><b></b>Rivo</div><div><b></b>Tallo</div><div><b></b>Chirpa</div></div>
  <div class="abs footer-links"><span>Home</span><span>About</span><span>Contact</span></div>
  <div class="abs copyright">© 2008 - 2011 www.bitlocate.ie<br>Car Dismantlers &amp; Car Breakers Search for Ireland</div>
  <div class="abs footer-art" role="img" aria-label="Small car outline decoration"></div>
</footer>
</body>
</html>
```